Creative Businesss Card desgin!

Create a business card for our business Gleam window cleaning!
We are open to creative ideas as long as it maintains a professional image.

Target Market(s)

Small Commercial window cleaning clients including car dealerships, strata manager, cafe

Industry/Entity Type

Window Cleaning

Contact Information for Business Card

Daniel Prescott
General Manager
Gleam Window Cleaning

daniel@gleamservices.com.au
pane-care-southbank.com.au
Ph: 1800 GET GLEAM
Mob: 0437 582 061

Colors
fbed22
0392cd

Requirements
Should not have
• Stock window cleaning/ squeegee graphics

```html
<!DOCTYPE html>
<html lang="en">
<head>
<meta charset="utf-8">
<title>Gleam Window Cleaning – Business Card</title>
<link href="https://fonts.googleapis.com/css2?family=Roboto:wght@400;500;700&display=swap" rel="stylesheet">
<style>
  :root {
    --gleam-blue: #04568a;
    --gleam-yellow: #f8ec21;
    --backdrop: #cfc6ba;
    --card-shadow: 0 6px 14px rgba(0,0,0,0.35);
  }
  * { margin: 0; padding: 0; box-sizing: border-box; }
  html, body { width: 900px; height: 1200px; overflow: hidden; }
  body {
    background: var(--backdrop);
    font-family: "Roboto", Arial, sans-serif;
    position: relative;
  }
  .card {
    position: absolute;
    left: 88px;
    width: 732px;
    height: 428px;
    border-radius: 22px;
    overflow: hidden;
    box-shadow: var(--card-shadow);
  }
  .card-front { top: 126px; background: var(--gleam-blue); color: var(--gleam-yellow); }
  .card-back { top: 641px; background: var(--gleam-yellow); color: var(--gleam-blue); }

  .front-waves { position: absolute; inset: 0; width: 732px; height: 428px; }

  .holder { position: absolute; right: 48px; top: 49px; text-align: right; color: var(--gleam-blue); }
  .holder-name { font-size: 19.5px; font-weight: 700; letter-spacing: 0.3px; line-height: 22px; }
  .holder-title { font-size: 15px; font-weight: 500; letter-spacing: 0.2px; line-height: 22px; }

  .wordmark { position: absolute; font-weight: 700; line-height: 1; white-space: nowrap; }
  .wordmark-name { display: block; font-size: 72px; letter-spacing: 1px; }
  .wordmark-tag { display: block; font-size: 26px; letter-spacing: 0.2px; margin-top: 6px; }
  .card-front .wordmark { left: 50px; top: 118px; }
  .card-back .wordmark { left: 0; right: 0; top: 150px; text-align: center; }

  .divider { position: absolute; left: 50px; right: 48px; top: 245px; height: 1px; background: var(--gleam-yellow); opacity: 0.85; }

  .contact-list { position: absolute; top: 262px; list-style: none; font-size: 16px; }
  .contact-list li { display: flex; align-items: center; height: 29px; gap: 11px; }
  .contact-phones { left: 50px; }
  .contact-online { right: 50px; }
  .contact-online li { justify-content: flex-end; }
  .contact-icon { width: 21px; height: 21px; flex: none; }

  .back-url { position: absolute; left: 0; right: 0; top: 364px; text-align: center; font-size: 16px; font-weight: 500; }
</style>
</head>
<body>

<section class="card card-front" aria-label="Business card front">
  <svg class="front-waves" viewBox="0 0 732 428" aria-hidden="true">
    <path fill="var(--gleam-yellow)" d="M340 0 C420 0 465 78 540 114 C585 136 630 138 732 138 V0 Z"/>
    <path fill="var(--gleam-yellow)" d="M0 428 V392 C38 388 70 402 102 428 Z"/>
  </svg>

  <div class="holder">
    <p class="holder-name">DANIEL PRESCOTT</p>
    <p class="holder-title">GENERAL MANAGER</p>
  </div>

  <div class="wordmark">
    <span class="wordmark-name">GLEAM</span>
    <span class="wordmark-tag">WINDOW CLEANING</span>
  </div>

  <div class="divider"></div>

  <ul class="contact-list contact-phones">
    <li>
      <svg class="contact-icon" viewBox="0 0 21 21" aria-hidden="true">
        <rect width="21" height="21" rx="4" fill="var(--gleam-yellow)"/>
        <path d="M5 8 C5 6 7 5.5 10.5 5.5 S16 6 16 8 L14 9 L13 8 H8 L7 9 Z" fill="var(--gleam-blue)"/>
        <rect x="6.5" y="10" width="8" height="5.5" rx="1" fill="var(--gleam-blue)"/>
      </svg>
      <span>1800 GET GLEAM</span>
    </li>
    <li>
      <svg class="contact-icon" viewBox="0 0 21 21" aria-hidden="true">
        <rect width="21" height="21" rx="4" fill="var(--gleam-yellow)"/>
        <rect x="7" y="4" width="7" height="13" rx="1.2" fill="var(--gleam-blue)"/>
        <rect x="8.2" y="5.5" width="4.6" height="7" fill="var(--gleam-yellow)"/>
      </svg>
      <span>0437 582 061</span>
    </li>
  </ul>

  <ul class="contact-list contact-online">
    <li>
      <span>daniel@gleamservices.com.au</span>
      <svg class="contact-icon" viewBox="0 0 21 21" aria-hidden="true">
        <rect width="21" height="21" rx="4" fill="var(--gleam-yellow)"/>
        <rect x="5" y="6.5" width="11" height="8" fill="none" stroke="var(--gleam-blue)" stroke-width="1.4"/>
        <path d="M5 6.5 L10.5 11 L16 6.5" fill="none" stroke="var(--gleam-blue)" stroke-width="1.4"/>
      </svg>
    </li>
    <li>
      <span>pane-care-southbank.com.au</span>
      <svg class="contact-icon" viewBox="0 0 21 21" aria-hidden="true">
        <rect width="21" height="21" rx="4" fill="var(--gleam-yellow)"/>
        <g fill="none" stroke="var(--gleam-blue)" stroke-width="1.2">
          <circle cx="10.5" cy="10.5" r="5.5"/>
          <ellipse cx="10.5" cy="10.5" rx="2.5" ry="5.5"/>
          <path d="M5 10.5 H16 M6 7.8 H15 M6 13.2 H15"/>
        </g>
      </svg>
    </li>
  </ul>
</section>

<section class="card card-back" aria-label="Business card back">
  <div class="wordmark">
    <span class="wordmark-name">GLEAM</span>
    <span class="wordmark-tag">WINDOW CLEANING</span>
  </div>
  <p class="back-url">pane-care-southbank.com.au</p>
</section>

</body>
</html>
```